Website for Fashion/Jewelry online seller

We would like a website design that can be used in wordpress. It will be important to be able to link instagram, twitter, etc posts on the bottom of site. We are to be a online seller of chic jewelry, art, fashion, and other home design industries. Currently we emphasize jewelry but as the years move forward, other products will be introduced as collections in home furnishings and primarily women's fashion. It will be important to have a “shop now” section where people can order products online so ecommerce will need to be set up at some point. The website should have the following feel: clean, modern, contemporary and chic. A lot of whites should be used with simple text and simple but elegant fonts. Best is to go to mirevatolkin.example to get the best idea of what we are wanting for the look and feel of the site.

Target Market(s)

upper social class people that are into fashion, jewelry, etc

Industry/Entity Type

Fashion

Number of Pages Required

5+ page

Font styles to use
Other font styles liked:
• go to karodwen.example to see the font desired

Requirements
Must have
• Name of Company is Tide Harbor 7
Nice to have
• see project description
Should not have
• see project description

```html
<!DOCTYPE html>
<html lang="en">
<head>
<meta charset="utf-8">
<title>Tide Harbor 7 — Chic Jewelry &amp; Fashion</title>
<link href="https://fonts.googleapis.com/css2?family=Poppins:wght@400;500;600;700&family=Open+Sans:wght@400;600&family=Great+Vibes&display=swap" rel="stylesheet">
<style>
:root{
  --gold:#f7b82b;
  --ink:#222222;
  --text:#555555;
  --header:#3b3b3b;
  --header-dark:#2a2a2a;
  --footer:#2f2f2f;
  --footer-dark:#262626;
  --panel:#f4f4f4;
  --white:#ffffff;
}
*{margin:0;padding:0;box-sizing:border-box}
html,body{width:735px;height:1200px;overflow:hidden;background:var(--white)}
body{position:relative;font-family:"Open Sans",Arial,sans-serif;color:var(--text)}
.abs{position:absolute}

/* Header */
.site-header{left:0;top:0;width:735px;height:40px;background:var(--header)}
.nav-item{top:0;height:40px;line-height:40px;font-family:"Poppins",Arial,sans-serif;font-size:9px;color:var(--gold);display:flex;align-items:center;gap:4px}
.brand{left:259px;top:0;width:217px;height:40px;background:var(--header-dark);display:flex;align-items:center;justify-content:center;font-family:"Poppins",Arial,sans-serif;font-weight:600;font-size:17px;color:var(--white);letter-spacing:.3px}

/* Hero */
.hero{left:0;top:40px;width:735px;height:370px;background:linear-gradient(180deg,#cfc3b6 0%,#b9a595 45%,#8a7564 75%,#3a3440 100%)}
.hero-kicker{left:0;top:170px;width:735px;text-align:center;font-family:"Poppins",Arial,sans-serif;font-weight:600;font-size:14px;letter-spacing:3px;color:var(--white)}
.hero-title{left:0;top:188px;width:735px;text-align:center;font-family:"Great Vibes",cursive;font-size:62px;line-height:64px;color:var(--white)}
.hero-btn{left:316px;top:256px;width:103px;height:24px;background:var(--gold);border-radius:2px;font-family:"Poppins",Arial,sans-serif;font-weight:600;font-size:12px;letter-spacing:2px;color:var(--ink);display:flex;align-items:center;justify-content:center}
.slide-tab{top:205px;width:13px;height:41px;background:#2b2b2b;border-radius:2px;color:var(--white);font-family:"Poppins",Arial,sans-serif;font-size:5.5px;line-height:7px;text-align:center;padding-top:6px}

/* Section titles */
.section-title{font-family:"Poppins",Arial,sans-serif;font-weight:500;font-size:24px;color:var(--gold);letter-spacing:.5px;text-align:center}
.section-lead{left:200px;top:464px;width:335px;text-align:center;font-size:7.2px;line-height:10.5px;color:#555}

/* Tiles */
.photo{display:block}
.tile-panel{background:var(--panel)}
.script{font-family:"Great Vibes",cursive;font-size:15px;color:var(--ink)}
.tile-title{font-family:"Poppins",Arial,sans-serif;font-weight:500;font-size:13px;color:var(--ink);letter-spacing:.4px}
.tile-price{font-size:8px;color:var(--text)}
.tile-price b{font-weight:400;color:var(--gold)}
.outline-btn{height:15px;border:1px solid var(--gold);font-family:"Poppins",Arial,sans-serif;font-size:7.5px;letter-spacing:1.4px;color:var(--ink);display:flex;align-items:center;justify-content:center;background:var(--white)}
.tile-band{background:rgba(245,240,236,.72);display:flex;flex-direction:column;align-items:center;justify-content:center}

/* Popular */
.arrow-btn{top:887px;width:16px;height:15px;background:var(--gold);border-radius:1px;display:flex;align-items:center;justify-content:center}
.thumb{top:921px;width:105px;height:112px}

/* Footer */
.footer-links{left:0;top:1046px;width:735px;display:flex;justify-content:center;gap:14px;font-family:"Poppins",Arial,sans-serif;font-size:8px;color:var(--ink)}
.site-footer{left:0;top:1072px;width:735px;height:103px;background:var(--footer)}
.footer-col{top:1072px;width:245px;height:103px;text-align:center}
.footer-col h3{margin-top:22px;font-family:"Poppins",Arial,sans-serif;font-weight:500;font-size:11px;color:var(--gold);letter-spacing:.5px}
.footer-col p{font-size:6.8px;color:#cfcfcf;line-height:14px}
.contact-line{display:flex;align-items:center;justify-content:center;gap:4px;font-size:6.8px;color:#cfcfcf;height:14px}
.contact-line.mail{color:var(--gold)}
.social{display:flex;justify-content:center;gap:9px;margin-top:8px}
.social span{width:23px;height:20px;border:1px solid #555;display:flex;align-items:center;justify-content:center}
.social span i{width:5px;height:5px;border-radius:50%;background:#bbb;display:block}
.newsletter{margin:8px auto 0;width:183px;height:22px;display:flex}
.newsletter .field{flex:1;border:1px solid #4a4a4a;font-size:5.6px;color:#9a9a9a;text-align:left;padding-left:9px;line-height:20px}
.newsletter .go{width:23px;background:var(--gold);display:flex;align-items:center;justify-content:center}
.copyright{left:0;top:1182px;width:735px;text-align:center;font-size:7px;color:#777}
</style>
</head>
<body>

<!-- Header -->
<header class="site-header abs"></header>
<div class="nav-item abs" style="left:29px">
  <svg width="7" height="6" viewBox="0 0 7 6"><rect y="0" width="7" height="1" fill="#f7b82b"/><rect y="2.5" width="7" height="1" fill="#f7b82b"/><rect y="5" width="7" height="1" fill="#f7b82b"/></svg>MENU</div>
<div class="nav-item abs" style="left:163px">
  <svg width="7" height="8" viewBox="0 0 7 8"><circle cx="3.5" cy="2" r="2" fill="#f7b82b"/><path d="M0 8a3.5 3.5 0 0 1 7 0z" fill="#f7b82b"/></svg>MY ACCOUNT</div>
<div class="brand abs">Tide Harbor 7</div>
<div class="nav-item abs" style="left:494px">
  <svg width="9" height="8" viewBox="0 0 9 8"><path d="M0 .5h1.6l1.2 5h5l1-3.6H2.4" fill="none" stroke="#f7b82b" stroke-width="1.2"/><circle cx="3.4" cy="7.2" r=".8" fill="#f7b82b"/><circle cx="7.2" cy="7.2" r=".8" fill="#f7b82b"/></svg>CART(0)</div>
<div class="nav-item abs" style="left:660px">
  <svg width="8" height="8" viewBox="0 0 8 8"><circle cx="3.2" cy="3.2" r="2.4" fill="none" stroke="#f7b82b" stroke-width="1.3"/><path d="M5 5l2.5 2.5" stroke="#f7b82b" stroke-width="1.4"/></svg>SEARCH</div>

<!-- Hero -->
<div class="hero abs" role="img" aria-label="Fashion photograph of a model seated on a brass bed with fur throw"></div>
<div class="slide-tab abs" style="left:30px">P<br>R<br>E<br>V</div>
<div class="slide-tab abs" style="left:690px">N<br>E<br>X<br>T</div>
<div class="hero-kicker abs">NEW TREND</div>
<div class="hero-title abs">Huge Collection</div>
<div class="hero-btn abs">SHOP NOW</div>
<svg class="abs" style="left:361px;top:366px" width="12" height="20" viewBox="0 0 12 20"><path d="M6 0v18M1 13l5 5 5-5" fill="none" stroke="#fff" stroke-width="1.6"/></svg>

<!-- Latest in -->
<h2 class="section-title abs" style="left:0;top:428px;width:735px">LATEST IN</h2>
<p class="section-lead abs">Lorem ipsum dolor sit amet, consectetuer adipiscing elit, sed diam nonummy nibh euismod tincidunt ut laoreet dolore magna aliquam erat volutpat.</p>

<div class="photo abs" style="left:30px;top:502px;width:215px;height:174px;background:linear-gradient(135deg,#d9d2c6,#6f7483 45%,#b8ab96)" role="img" aria-label="Grey leather wrap bracelets with silver and gold medallions"></div>
<div class="tile-panel abs" style="left:245px;top:502px;width:204px;height:174px"></div>
<div class="script abs" style="left:265px;top:530px">emphasize jewelry</div>
<div class="tile-title abs" style="left:265px;top:560px">NEW PRODUCTS</div>
<div class="tile-price abs" style="left:265px;top:579px">From to <b>$30.00</b></div>
<div class="outline-btn abs" style="left:265px;top:618px;width:67px">SHOP NOW</div>

<div class="photo abs" style="left:449px;top:502px;width:256px;height:174px;background:linear-gradient(180deg,#d8dde0,#8c6e62 50%,#7d7478)" role="img" aria-label="Sparkling bronze cuff bracelet with druzy stone"></div>
<div class="tile-band abs" style="left:449px;top:557px;width:256px;height:65px">
  <div class="script">chic jewelry</div>
  <div class="tile-title" style="margin-top:2px">HOMEBASE</div>
</div>

<div class="photo abs" style="left:30px;top:676px;width:256px;height:175px;background:linear-gradient(160deg,#5fa6b6,#8b5a36 40%,#c9c3b8 75%,#9c6b3e)" role="img" aria-label="Turquoise bead necklaces with silver saint medals on wood"></div>
<div class="tile-band abs" style="left:30px;top:731px;width:256px;height:65px">
  <div class="script">chic jewelry</div>
  <div class="tile-title" style="margin-top:2px">HOME DESIGN</div>
</div>
<div class="photo abs" style="left:286px;top:676px;width:215px;height:175px;background:linear-gradient(180deg,#e4e1dd,#c9b8a7 55%,#2e2c3a)" role="img" aria-label="Fashion photograph of a model on a brass bed"></div>
<div class="tile-panel abs" style="left:501px;top:676px;width:204px;height:175px"></div>
<div class="script abs" style="left:522px;top:705px">women's fashion</div>
<div class="tile-title abs" style="left:522px;top:734px">NEW PRODUCTS</div>
<div class="tile-price abs" style="left:522px;top:753px">From to <b>$20.00</b></div>
<div class="outline-btn abs" style="left:522px;top:793px;width:66px">SHOP NOW</div>

<!-- Popular posts -->
<div class="arrow-btn abs" style="left:30px"><svg width="6" height="7" viewBox="0 0 6 7"><path d="M5 0v7L0 3.5z" fill="#222"/></svg></div>
<div class="arrow-btn abs" style="left:55px"><svg width="6" height="7" viewBox="0 0 6 7"><path d="M1 0v7l5-3.5z" fill="#222"/></svg></div>
<h2 class="section-title abs" style="left:0;top:877px;width:735px">POPULAR POSTS</h2>
<div class="outline-btn abs" style="left:638px;top:886px;width:65px;height:16px">VIEW ALL</div>

<div class="thumb abs" style="left:0;background:linear-gradient(135deg,#e9dfd4,#3c8f9c 50%,#b86b58)" role="img" aria-label="Beaded necklace on art cards"></div>
<div class="thumb abs" style="left:105px;background:linear-gradient(180deg,#f4d34a,#e9e4dc 45%,#7a5a3c)" role="img" aria-label="Yellow flowers in a vase on a tree stump"></div>
<div class="thumb abs" style="left:210px;background:linear-gradient(180deg,#dde1e3,#8a6e64 45%,#6e6a72)" role="img" aria-label="Bronze cuff bracelet"></div>
<div class="thumb abs" style="left:315px;background:linear-gradient(135deg,#c9cbd0,#6c717e 55%,#a9a8a8)" role="img" aria-label="Silver medallion on grey wrap bracelet"></div>
<div class="thumb abs" style="left:420px;background:linear-gradient(160deg,#3f8fa3,#7b4f30 50%,#c4beb4)" role="img" aria-label="Turquoise bead necklaces with medals"></div>
<div class="thumb abs" style="left:525px;background:linear-gradient(135deg,#d8d0c4,#1f2a7a 50%,#c9bfae)" role="img" aria-label="Navy wrap bracelets with gold charm"></div>
<div class="thumb abs" style="left:630px;background:linear-gradient(135deg,#2a7f9d,#3bb5cf 50%,#1d5c78)" role="img" aria-label="Turquoise wrap bracelets with gold chains"></div>

<!-- Footer -->
<nav class="footer-links abs">
  <span>SHOP</span><span>-</span><span>ABOUT</span><span>-</span><span>CHARITY</span><span>-</span><span>LOCATIONS</span><span>-</span><span>CONTACT</span>
</nav>
<footer class="site-footer abs"></footer>
<div class="footer-col abs" style="left:0">
  <h3>CONTACT US</h3>
  <div class="contact-line" style="margin-top:8px"><svg width="5" height="7" viewBox="0 0 5 7"><path d="M2.5 7L.4 3.4A2.5 2.5 0 1 1 4.6 3.4z" fill="#bbb"/><circle cx="2.5" cy="2.4" r=".9" fill="#2f2f2f"/></svg>C - 234, Harbor building, St. Newport</div>
  <div class="contact-line"><svg width="6" height="6" viewBox="0 0 6 6"><path d="M1 0l1.3 1.5-.7 1a4 4 0 0 0 1.9 1.9l1-.7L6 5 5 6C2.3 6 0 3.7 0 1z" fill="#bbb"/></svg>(+222) 555 0134 210</div>
  <div class="contact-line mail"><svg width="7" height="5" viewBox="0 0 7 5"><rect x=".4" y=".4" width="6.2" height="4.2" fill="none" stroke="#bbb" stroke-width=".8"/><path d="M.4.4l3.1 2.4L6.6.4" fill="none" stroke="#bbb" stroke-width=".8"/></svg>contact@tideharbor7.example</div>
</div>
<div class="footer-col abs" style="left:245px;background:var(--footer-dark)">
  <h3>CONNECT WITH US</h3>
  <p style="margin-top:6px">Join the conversion about Tide Harbor 7</p>
  <div class="social"><span><i></i></span><span><i></i></span><span><i></i></span><span><i></i></span><span><i></i></span></div>
</div>
<div class="footer-col abs" style="left:490px">
  <h3>NEWSLETTER</h3>
  <p style="margin-top:6px">Lorem ipsum dolor sit consectetuer adipiscing elit</p>
  <div class="newsletter">
    <div class="field">Your email address...</div>
    <div class="go"><svg width="7" height="6" viewBox="0 0 7 6"><path d="M0 3h6M4 1l2 2-2 2" fill="none" stroke="#fff" stroke-width=".9"/></svg></div>
  </div>
</div>
<div class="copyright abs">All rights reserved. © 2016 Tide Harbor 7</div>

</body>
</html>
```